Studying Effectively To Do List

I am looking to design a new "Study To Do List" for High School students (Ages 15 - 18) . This will be printed as an A4 notepad and so should only be a single A4 page.

The Design will need to be professional and look semi-serious but also be appealing to High school students (Ages 15 - 18) and should NOT be gender specific.

I have attached a word document outlining the structure of the page. The space provided should be large enough that people can write in it comfortably.

The notepad will most likely be printed in black and white but I'm also looking at coloured options - colours should be kept to a minimum.

This will be printed professionally and should also include a 3mm bleed.

The design should also include the business logo (included in the word document)

Target Market(s)

High School students (Ages 15 - 18). Both genders

Industry/Entity Type

Education

Font styles to use
Serif
Sans Serif

Requirements
Must have
• Please see the word document attached.
Should not have
• Too much colour

```html
<!DOCTYPE html>
<html lang="en">
<head>
<meta charset="utf-8">
<title>Northfield Study To Do List</title>
<link href="https://fonts.googleapis.com/css2?family=Open+Sans:wght@400;600;700;800&display=swap" rel="stylesheet">
<style>
  :root {
    --orange: #f47a1f;
    --orange-deep: #ee6a10;
    --orange-light: #f89a45;
    --ink: #1f1f1f;
    --rule-dark: #3a3a3a;
    --paper: #f6f6f6;
    --paper-edge: #ececec;
    --charcoal: #444444;
    --backdrop: #e9e6e1;
  }
  * { box-sizing: border-box; margin: 0; padding: 0; }
  html, body {
    width: 1020px; height: 1200px; overflow: hidden;
    background: var(--backdrop);
    font-family: "Open Sans", Arial, sans-serif;
    color: var(--ink);
  }
  .sheet {
    position: absolute; left: 100px; top: 20px;
    width: 596px; height: 842px;
    transform: scale(1.3775); transform-origin: top left;
    background: linear-gradient(160deg, #ffffff 0%, var(--paper) 55%, var(--paper-edge) 100%);
    overflow: hidden;
  }
  .header-band { position: absolute; left: 0; top: 0; width: 596px; height: 130px; }
  .brand {
    position: absolute; left: 30px; top: 60px;
    display: flex; align-items: center; gap: 5px;
  }
  .brand-dot { width: 14px; height: 14px; border-radius: 50%; background: var(--orange); }
  .brand-name { font-size: 15px; font-weight: 700; color: var(--charcoal); }
  .website {
    position: absolute; right: 16px; top: 22px;
    display: flex; align-items: center; gap: 6px;
    color: #fff; font-size: 14px;
  }
  .watermark {
    position: absolute; left: 143px; top: 262px; width: 260px; height: 260px;
    border: 16px solid rgba(120,120,120,0.08); border-radius: 50%;
    display: flex; align-items: center; justify-content: center;
  }
  .watermark span { font-size: 40px; font-weight: 700; color: rgba(120,120,120,0.09); }
  .pill {
    position: absolute; left: 50%; transform: translateX(-50%);
    background: var(--orange); color: #fff;
    font-size: 11px; font-weight: 700; letter-spacing: 0.2px;
    padding: 4px 15px; border-radius: 3px;
    box-shadow: 0 2px 3px rgba(0,0,0,0.25);
  }
  .date { position: absolute; left: 429px; top: 120px; font-size: 11px; display: flex; width: 153px; }
  .fill { flex: 1; border-bottom: 1px solid var(--rule-dark); margin-left: 2px; margin-bottom: 3px; }
  .grid { position: absolute; left: 14px; width: 568px; border-collapse: collapse; }
  .grid td {
    border: 1px solid var(--rule-dark); height: 19px; padding: 0 8px;
    font-size: 10px; font-weight: 700; vertical-align: middle;
  }
  .grid th {
    background: var(--orange); color: #fff; font-size: 10px; font-weight: 700;
    height: 18px; border: 1px solid var(--orange);
  }
  .grid .plain { font-weight: 400; }
  .lines { position: absolute; left: 15px; width: 567px; }
  .line { display: flex; align-items: flex-end; height: 15.8px; font-size: 10px; }
  .line .fill { margin-bottom: 2px; }
  .line.subject, .line.element { color: var(--orange); }
  .line.subject .fill, .line.element .fill { border-bottom-color: var(--orange); }
  .line.assessment { height: 16.5px; }
  .line.element { height: 16.5px; }
  .line .short { flex: 0 0 212px; }
  .line .due { margin: 0 5px; }
  .footer-bar { position: absolute; left: 0; bottom: 0; width: 596px; height: 8px; display: flex; }
  .footer-bar .left { flex: 1; background: var(--orange-deep); }
  .footer-bar .right { flex: 1; background: var(--charcoal); }
</style>
</head>
<body>
  <div class="sheet">
    <svg class="header-band" viewBox="0 0 596 130" aria-hidden="true">
      <polygon points="0,0 596,0 596,117 450,72 385,104 265,52 55,38 0,58" fill="var(--orange)"/>
      <polygon points="0,0 596,0 596,20 330,28 200,18 55,38 0,18" fill="var(--orange-light)"/>
      <polygon points="330,28 596,20 596,75 460,40" fill="var(--orange-deep)" opacity="0.6"/>
    </svg>

    <div class="brand">
      <div class="brand-dot"></div>
      <div class="brand-name">Northfield</div>
    </div>

    <div class="website">
      <svg width="13" height="13" viewBox="0 0 14 14" aria-hidden="true">
        <g fill="none" stroke="#fff" stroke-width="1.2">
          <circle cx="7" cy="7" r="6"/>
          <ellipse cx="7" cy="7" rx="2.6" ry="6"/>
          <line x1="1" y1="7" x2="13" y2="7"/>
        </g>
      </svg>
      <span>www.northfieldstudy.com</span>
    </div>

    <div class="watermark" aria-hidden="true"><span>Northfield</span></div>

    <div class="pill" style="top:114px">REVISION</div>
    <div class="date">Date:<span class="fill"></span></div>

    <table class="grid" style="top:154px">
      <tr><td>1</td><td>5</td></tr>
      <tr><td>2</td><td>6</td></tr>
      <tr><td>3</td><td>7</td></tr>
      <tr><td>4</td><td>8</td></tr>
    </table>

    <div class="pill" style="top:246px">HOMEWORK</div>
    <div class="lines" style="top:273px">
      <div class="line subject">Subject:<span class="fill"></span></div>
      <div class="line task">Task:<span class="fill"></span></div>
      <div class="line subject">Subject:<span class="fill"></span></div>
      <div class="line task">Task:<span class="fill"></span></div>
      <div class="line subject">Subject:<span class="fill"></span></div>
      <div class="line task">Task:<span class="fill"></span></div>
      <div class="line subject">Subject:<span class="fill"></span></div>
      <div class="line task">Task:<span class="fill"></span></div>
      <div class="line subject">Subject:<span class="fill"></span></div>
      <div class="line task">Task:<span class="fill"></span></div>
      <div class="line subject">Subject:<span class="fill"></span></div>
      <div class="line task">Task:<span class="fill"></span></div>
    </div>

    <div class="pill" style="top:470px">ASSESSMENTS</div>
    <div class="lines" style="top:500px">
      <div class="line assessment">Assessment:<span class="fill short"></span><span class="due">Due</span><span class="fill"></span></div>
      <div class="line element">Element:<span class="fill"></span></div>
      <div class="line assessment">Assessment:<span class="fill short"></span><span class="due">Due</span><span class="fill"></span></div>
      <div class="line element">Element:<span class="fill"></span></div>
      <div class="line assessment">Assessment:<span class="fill short"></span><span class="due">Due</span><span class="fill"></span></div>
      <div class="line element">Element:<span class="fill"></span></div>
      <div class="line assessment">Assessment:<span class="fill short"></span><span class="due">Due</span><span class="fill"></span></div>
      <div class="line element">Element:<span class="fill"></span></div>
      <div class="line assessment">Assessment:<span class="fill short"></span><span class="due">Due</span><span class="fill"></span></div>
      <div class="line element">Element:<span class="fill"></span></div>
      <div class="line assessment">Assessment:<span class="fill short"></span><span class="due">Due</span><span class="fill"></span></div>
      <div class="line element">Element:<span class="fill"></span></div>
    </div>

    <table class="grid" style="top:720px">
      <tr><th colspan="2">NOTES</th><th style="font-size:9px">PRACTICE</th></tr>
      <tr><td style="width:142px">1</td><td style="width:142px"></td><td>5</td></tr>
      <tr><td>2</td><td></td><td>6</td></tr>
      <tr><td>3</td><td></td><td>7</td></tr>
      <tr><td>4</td><td></td><td class="plain">8</td></tr>
    </table>

    <div class="footer-bar"><div class="left"></div><div class="right"></div></div>
  </div>
</body>
</html>
```